Duel Business card

Want an edgy business card that shows both of our companies on each side of the card, OR both together with a cool design.

*Must be edgy: We have attached our two business logos. We are a bail bond and immigration bond company.

Would like the address on one side only.
Need Phone, cell, website, address, and Name

Company Name 1: Cellgate Release Partners
www.cellgatereleasepartners.example

Company Name 2: Borderline Surety Associates
www.borderlinesuretyassociates.example

These cards will need to be easily changeable so I can modify new employees

Target Market(s)

people in jail, takign imigrants out of jail and from being taken back to there country

Industry/Entity Type

Business

Requirements
Must have
• Include both logos attached

```html
<!DOCTYPE html>
<html lang="en">
<head>
<meta charset="utf-8">
<title>Dual Business Card</title>
<link rel="stylesheet" href="https://fonts.googleapis.com/css2?family=Roboto:wght@400;700;900&display=swap">
<style>
  :root {
    --backdrop: #b5b5b5;
    --navy: #022f87;
    --yellow: #f1c816;
    --red: #e33426;
    --paper: #ffffff;
    --mist: #eeeeee;
    --ink: #1f1f1f;
    --rule: #333333;
  }
  * { margin: 0; padding: 0; box-sizing: border-box; }
  html, body { width: 1200px; height: 602px; overflow: hidden; }
  body { background: var(--backdrop); font-family: "Roboto", Arial, sans-serif; position: relative; }

  .card { position: absolute; width: 510px; height: 307px; overflow: hidden; box-shadow: 2px 4px 8px rgba(0,0,0,.28); }

  /* Front */
  .card-front { left: 56px; top: 56px; background: var(--mist); }
  .front-half { position: absolute; top: 0; width: 255px; height: 280px; display: flex; align-items: center; justify-content: center; flex-direction: column; gap: 10px; }
  .front-half--bail { left: 0; background: var(--navy); }
  .front-half--immigration { left: 255px; background: var(--mist); }
  .front-strip { position: absolute; top: 280px; height: 27px; width: 255px; }
  .front-strip--yellow { left: 0; background: var(--yellow); }
  .front-strip--red { left: 255px; background: var(--red); }

  .brand-dot { width: 46px; height: 46px; border-radius: 50%; border: 3px solid var(--yellow); }
  .brand-dot--red { border-color: var(--red); background: var(--paper); }
  .brand-name { font-weight: 900; font-size: 19px; line-height: 1.05; text-align: center; text-transform: uppercase; letter-spacing: .3px; }
  .brand-name--bail { color: var(--paper); }
  .brand-name--immigration { color: var(--navy); }

  /* Back */
  .card-back { left: 634px; top: 238px; height: 308px; background: var(--paper); }
  .holder { position: absolute; left: 28px; top: 33px; display: flex; align-items: center; gap: 10px; }
  .holder-name { font-size: 23px; font-weight: 700; color: var(--navy); white-space: nowrap; }
  .holder-stripe { width: 290px; height: 14px; background: var(--red); }

  .band { position: absolute; width: 255px; }
  .band--blue { left: 0; top: 78px; height: 113px; background: var(--navy); }
  .band--yellow { left: 255px; top: 78px; height: 113px; background: var(--yellow); }
  .band--red { left: 0; top: 191px; height: 117px; background: var(--red); }
  .band--mist { left: 255px; top: 191px; height: 117px; background: var(--mist); }

  .contact-panel { position: absolute; left: 29px; top: 104px; width: 453px; height: 176px; background: var(--paper); }
  .contact-row { position: absolute; left: 0; width: 100%; height: 87px; display: flex; align-items: center; }
  .contact-row--bail { top: 0; border-bottom: 2px solid var(--rule); }
  .contact-row--immigration { top: 89px; }
  .row-brand { width: 133px; display: flex; flex-direction: column; align-items: center; gap: 4px; }
  .row-brand .brand-dot { width: 22px; height: 22px; border-width: 2px; }
  .row-brand-name { font-size: 9px; font-weight: 900; line-height: 1.1; text-align: center; text-transform: uppercase; }
  .row-brand-name--bail { color: var(--navy); }
  .row-brand-name--immigration { color: var(--red); }

  .contact-details { font-size: 13.5px; line-height: 16px; color: var(--ink); }
  .company { font-weight: 700; font-size: 14px; }
  .company--bail { color: var(--navy); }
  .company--immigration { color: var(--red); }
  .label { font-weight: 700; font-style: italic; }
</style>
</head>
<body>

<section class="card card-front">
  <div class="front-half front-half--bail">
    <div class="brand-dot"></div>
    <div class="brand-name brand-name--bail">Cellgate<br>Release Partners</div>
  </div>
  <div class="front-half front-half--immigration">
    <div class="brand-dot brand-dot--red"></div>
    <div class="brand-name brand-name--immigration">Borderline<br>Surety Associates</div>
  </div>
  <div class="front-strip front-strip--yellow"></div>
  <div class="front-strip front-strip--red"></div>
</section>

<section class="card card-back">
  <div class="holder">
    <span class="holder-name">Daniel Verano</span>
    <div class="holder-stripe" role="img" aria-label="Red slash stripe ornament"></div>
  </div>

  <div class="band band--blue"></div>
  <div class="band band--yellow"></div>
  <div class="band band--red"></div>
  <div class="band band--mist"></div>

  <div class="contact-panel">
    <div class="contact-row contact-row--bail">
      <div class="row-brand">
        <div class="brand-dot"></div>
        <div class="row-brand-name row-brand-name--bail">Cellgate<br>Release Partners</div>
      </div>
      <div class="contact-details">
        <div class="company company--bail">Cellgate Release Partners Las Vegas</div>
        <div>418 N. Harbor Crest Ave. Las Vegas, NV 89101</div>
        <div><span class="label">t</span>. 1-888-555-0147 &nbsp; <span class="label">m</span>. 775-555-0163</div>
        <div>www.cellgatereleasepartners.example</div>
      </div>
    </div>
    <div class="contact-row contact-row--immigration">
      <div class="row-brand">
        <div class="brand-dot brand-dot--red"></div>
        <div class="row-brand-name row-brand-name--immigration">Borderline<br>Surety Associates</div>
      </div>
      <div class="contact-details">
        <div class="company company--immigration">Borderline Surety Associates Agency, LLC.</div>
        <div>418 N. Harbor Crest Ave. Las Vegas, NV 89101</div>
        <div><span class="label">t</span>. 877-555-0192 &nbsp; <span class="label">m</span>. 775-555-0163</div>
        <div>www.borderlinesuretyassociates.example</div>
      </div>
    </div>
  </div>
</section>

</body>
</html>
```